1. 商品のコンセプト:鉢植えの植物を元気にみずみずしく保つ。お客様に代わって心を込めたお手入れを。
2. 商品コンセプトの理由:水やり以外のお手入れは放置しがちな鉢植えも、お手入れすることで美しく保てることで、安らぎや楽しみを与えてくれる存在となります。
3. 販売価格:(価格はすべて税込み)
【植替え】
新しく植え替える鉢の上部直径
15㎝(5号鉢)まで 3,500円
21㎝(7号鉢)まで 6,000円
30㎝(10号鉢)まで 9,000円
45㎝(15号鉢)まで 15,000円
※ただし、盆栽は除く
●料金は作業代のみの価格となります。
●植替えで必要な鉢や土などは、お客さまがご用意いただければ別途費用がかからず、そちらを使用して作業致します。
ただし、樹種や状態によって必要な鉢のサイズや土の種類や量がありますので、お見積り時にご相談のうえご用意いただけるのが望ましいです。
●また、鉢や土など当社でご用意することも可能です。その場合、別途お見積りとなります。
●古い土は、ご希望があればお引き取りいたします(別途見積り)
●不要になった鉢のお引き取りは、ご相談ください(別途見積り)
※ただし、プラスチック、金属、ガラス、樹脂、コンクリートなどはお引き取りできません。
【剪定】形を整えたり、高さを調整したりします。
高さ3m未満 4,000円/本
【消毒】病害虫の症状にあわせた薬剤は散布し予防や駆除をします。
高さ3m未満 2,000円/本
【施肥】肥料を施して栄養分を補い、成育促進、花付き、実付きの改善をします。
3,000円より
4. 販売方法
お見積り無料
ご依頼(電話・WEB)→担当から連絡→無料見積り(お客様宅へ出向いて実際のものを見てお見積りをします。見積書有効期限1か月)→ご依頼(作業日時決定)→作業→お支払い(郵便局・銀行から振り込み、コンビニエンスストアでのお支払い(コンビニ後払い)、クレジットカード決済)

[強み]
1鉢からでも承ります。お見積り無料。お客さまご自身で植替えに必要な鉢や土などを担当者にご相談のうえご用意いただけたら、費用は作業代のみとなります(土やゴミの回収ご希望の場合は別途費用がかかります)
社名、ロゴ、電話番号、URL、QRコード
A4
両面
緑系、水色系、茶系、こだわりはそれ程強くないので、色合いはお任せします。
• イラストレーター形式 (.ai)
弊社HP
https://www.375m.co.jp/
各種メニューと価格
https://www.375m.co.jp/price/

鉢植えの植替えや鉢植えのお手入れに関する素材については、フリー素材等にて適宜入れてください。
必要に応じてリクエストさせていただきたいと思います。

必要な情報が一通り網羅されていました。
シンプルに当社のサービスを表現されていました。

短期間の中多くのご提案をいただき、誠にありがとうございました。
どのご提案もレベルが高く、良い意味で選定に苦慮しました。
また新たなチラシ作成の際は是非ご提案いただければ幸いです。

```html
<!DOCTYPE html>
<html lang="ja">
<head>
<meta charset="utf-8">
<title>鉢植えのお手入れ承ります</title>
<link rel="stylesheet" href="https://fonts.googleapis.com/css2?family=Dela+Gothic+One&family=M+PLUS+Rounded+1c:wght@500;800&family=Noto+Sans+JP:wght@400;700;900&display=swap">
<style>
  :root{
    --sky:#bfe7f4;
    --sky-deep:#8fd2e8;
    --teal:#1f9ca3;
    --leaf:#2d8f3e;
    --yellow:#ffe033;
    --yellow-dark:#e9c400;
    --red:#e8303a;
    --ink:#1a1a1a;
    --white:#ffffff;
  }
  *{margin:0;padding:0;box-sizing:border-box}
  html,body{width:861px;height:1200px;overflow:hidden;background:var(--white)}
  .flyer{position:relative;width:861px;height:1200px;overflow:hidden;
    background:radial-gradient(circle at 20% 85%,var(--sky-deep) 0,var(--sky) 40%),var(--sky);
    font-family:"Noto Sans JP",sans-serif;color:var(--ink)}
  .concept-band{position:absolute;left:0;top:18px;width:861px;height:44px;background:var(--teal);
    color:var(--white);font-weight:700;font-size:19px;line-height:44px;text-align:center;letter-spacing:.02em}
  .hero-photo{position:absolute;left:120px;top:70px;width:741px;height:560px;
    border-radius:280px 0 0 280px;
    background:linear-gradient(135deg,#d9d1b8 0%,#a48a5e 40%,#6d5236 70%,#c9a94a 100%)}
  .lead-note{position:absolute;left:40px;top:92px;transform:rotate(-10deg);
    font-family:"M PLUS Rounded 1c",sans-serif;font-weight:800;font-size:25px;line-height:1.3;color:var(--red);
    text-shadow:0 0 4px var(--white),0 0 4px var(--white),0 0 4px var(--white)}
  .estimate-badge{position:absolute;left:648px;top:140px;width:160px;height:160px;border-radius:50%;
    background:var(--white);border:4px solid var(--red);color:var(--red);text-align:center;
    display:flex;flex-direction:column;justify-content:center;font-weight:900}
  .estimate-badge .small{font-size:26px;line-height:1.1}
  .estimate-badge .big{font-size:50px;line-height:1.1}
  .headline{position:absolute;left:90px;top:360px;font-family:"Dela Gothic One",sans-serif;font-weight:400;
    font-size:118px;line-height:1.2;color:var(--white);transform:skewX(-6deg);
    -webkit-text-stroke:10px var(--ink);paint-order:stroke fill;z-index:2}
  .headline span{display:block}
  .headline .second{margin-left:20px}
  .tree-photo{position:absolute;left:700px;top:730px;width:120px;height:310px;border-radius:60px 60px 10px 10px;
    background:linear-gradient(180deg,#7fb24a 0%,#4e8a2e 45%,#8a6a3e 75%,#f2f2f0 100%);z-index:1}
  .accept{position:absolute;left:470px;top:670px;font-family:"Dela Gothic One",sans-serif;font-size:52px;
    color:var(--ink);text-shadow:2px 2px 0 var(--white);transform:rotate(-4deg);white-space:nowrap;z-index:3}
  .service-list{position:absolute;left:80px;top:790px;display:flex;gap:30px;list-style:none}
  .service{width:112px;text-align:center;color:var(--white);font-weight:700;font-size:22px}
  .service-icon{width:112px;height:98px;background:var(--yellow);display:flex;align-items:center;justify-content:center}
  .service-icon .mark{width:56px;height:56px;border-radius:50%;background:var(--yellow-dark)}
  .service-name{display:block;margin-top:6px;text-shadow:0 1px 3px rgba(0,0,0,.35)}
  .strength{position:absolute;left:70px;top:950px;font-weight:900;font-size:28px;color:var(--yellow);
    text-shadow:0 1px 3px rgba(0,0,0,.4)}
  .strength-note{position:absolute;left:70px;top:994px;width:600px;font-size:11.5px;line-height:1.45;color:var(--white)}
  .footer{position:absolute;left:0;top:1060px;width:861px;height:140px;background:var(--white);
    display:flex;align-items:center;padding:0 26px;gap:24px}
  .brand{display:flex;flex-direction:column;color:var(--leaf);font-weight:900}
  .brand .roman{font-size:12px;letter-spacing:.15em}
  .brand .name{font-size:34px;line-height:1.1}
  .contact{display:flex;flex-direction:column;gap:2px}
  .hours{font-size:13px;font-weight:700}
  .hours b{background:var(--ink);color:var(--white);padding:0 6px;margin-right:6px;font-size:12px}
  .phone{display:flex;align-items:center;gap:6px;font-size:38px;font-weight:900;line-height:1}
  .url{font-size:14px;font-weight:700}
  .url b{background:var(--ink);color:var(--white);padding:0 5px;margin-right:6px;font-size:12px}
  .more{margin-left:auto;background:var(--leaf);color:var(--white);font-weight:700;font-size:17px;
    line-height:1.35;padding:12px 16px;text-align:center;display:flex;align-items:center;gap:8px}
</style>
</head>
<body>
<main class="flyer">
  <p class="concept-band">鉢植えの植物を元気にみずみずしく保つ。お客様に代わって心を込めたお手入れを。</p>

  <div class="hero-photo" role="img" aria-label="鉢植えの土を手で整えている植替え作業の写真"></div>

  <p class="lead-note">放置しがちな<br>鉢植えのお手入れは<br>プロにお任せ!</p>

  <div class="estimate-badge">
    <span class="small">お見積り</span>
    <span class="big">無料</span>
  </div>

  <h1 class="headline"><span>鉢植えの</span><span class="second">お手入れ</span></h1>

  <div class="tree-photo" role="img" aria-label="白い鉢に植えられたレモンの木の写真"></div>

  <p class="accept">承ります!</p>

  <ul class="service-list">
    <li class="service"><div class="service-icon"><div class="mark" role="img" aria-label="植替えのアイコン"></div></div><span class="service-name">植替え</span></li>
    <li class="service"><div class="service-icon"><div class="mark" role="img" aria-label="剪定ばさみのアイコン"></div></div><span class="service-name">剪定</span></li>
    <li class="service"><div class="service-icon"><div class="mark" role="img" aria-label="若葉と消毒のアイコン"></div></div><span class="service-name">消毒</span></li>
    <li class="service"><div class="service-icon"><div class="mark" role="img" aria-label="肥料袋のアイコン"></div></div><span class="service-name">施肥</span></li>
  </ul>

  <p class="strength">1鉢からでも承ります。お見積り無料。</p>
  <p class="strength-note">お客さまご自身で植替えに必要な鉢や土などを担当者にご相談のうえご用意いただけたら、費用は作業代のみとなります。<br>(土やゴミの回収ご希望の場合は別途費用がかかります)</p>

  <footer class="footer">
    <div class="brand"><span class="roman">NIWAKI KOBO MIDORI</span><span class="name">庭木工房みどり</span></div>
    <div class="contact">
      <p class="hours"><b>受付時間</b>AM9:00-PM18:00</p>
      <p class="phone">
        <svg width="34" height="34" viewBox="0 0 24 24" aria-hidden="true"><path fill="#1a1a1a" d="M6.6 10.8a15.1 15.1 0 0 0 6.6 6.6l2.2-2.2c.3-.3.7-.4 1-.2 1.1.4 2.3.6 3.6.6.6 0 1 .4 1 1V20c0 .6-.4 1-1 1A17 17 0 0 1 3 4c0-.6.4-1 1-1h3.5c.6 0 1 .4 1 1 0 1.3.2 2.5.6 3.6.1.3 0 .7-.2 1z"/></svg>
        0120-375-375
      </p>
      <p class="url"><b>HP</b>https://www.375m.co.jp/</p>
    </div>
    <div class="more">
      <span>詳しくは裏面を<br>ご覧下さい</span>
      <svg width="14" height="20" viewBox="0 0 14 20" aria-hidden="true"><path d="M2 2l9 8-9 8" fill="none" stroke="#fff" stroke-width="3"/></svg>
    </div>
  </footer>
</main>
</body>
</html>
```